Stationery for Services Company
Business Cards, Letterhead and Compliment Slips
Hi FenwickStudio,
We really like Draft 15. There are a few small changes though:-
1. On the bus cards and letterhead the phone number ends with 667 and not 668 as previously advised. Could this please be amended.
2.On the letterhead at the bottom could we remove mobile phone number and instead include website address: www.norvelpartners.com, the main telephone number ending in 667 and a general e-mail address: info@norvelpartners.com.
Many Thanks,
C.

```html
<!DOCTYPE html>
<html lang="en">
<head>
<meta charset="utf-8">
<title>Norvel Partners Stationery</title>
<link href="https://fonts.googleapis.com/css2?family=PT+Sans:wght@400;700&display=swap" rel="stylesheet">
<style>
  :root {
    --navy: #24428a;
    --gold: #a8923f;
    --gold-light: #c4b16c;
    --ink: #333a4a;
    --paper: #ffffff;
    --canvas: #ffffff;
  }
  * { box-sizing: border-box; margin: 0; padding: 0; }
  html, body { width: 1200px; height: 859px; overflow: hidden; background: var(--canvas); }
  body { position: relative; font-family: "PT Sans", Arial, sans-serif; color: var(--ink); }
  address { font-style: normal; }

  .sheet { position: absolute; background: var(--paper); box-shadow: 0 0 3px rgba(0,0,0,.25); overflow: hidden; }
  .brand { display: flex; align-items: center; gap: 6px; color: var(--navy); font-weight: 700; white-space: nowrap; }
  .brand-dot { border-radius: 50%; background: var(--gold); flex: none; }
  .contact { position: absolute; border-left: 1px solid var(--gold); padding-left: 6px; color: var(--navy); line-height: 1.35; white-space: nowrap; }
  .band { position: absolute; left: 0; right: 0; bottom: 0; display: flex; }
  .band-gold { background: var(--gold); flex: 1; }
  .band-light { background: var(--gold-light); }
  .band-navy { background: var(--navy); }

  /* Letterhead */
  .letterhead { left: 14px; top: 10px; width: 640px; height: 818px; }
  .letterhead .brand { position: absolute; left: 30px; top: 58px; font-size: 22px; }
  .letterhead .brand-dot { width: 14px; height: 14px; }
  .letterhead .contact { left: 510px; top: 40px; font-size: 8px; }
  .letterhead .footer-info { position: absolute; left: 0; right: 0; bottom: 22px; display: flex; justify-content: center; gap: 22px; font-size: 8px; color: var(--navy); }
  .letterhead .band { height: 12px; }
  .letterhead .band-light { width: 6px; }
  .letterhead .band-navy { width: 44px; }

  /* Compliment slip */
  .slip { left: 473px; top: 168px; width: 704px; height: 302px; }
  .slip .brand { position: absolute; left: 22px; top: 50px; font-size: 22px; }
  .slip .brand-dot { width: 14px; height: 14px; }
  .slip .contact { left: 230px; top: 46px; font-size: 8.5px; }
  .slip .band { height: 12px; }
  .slip .band-light { width: 8px; }
  .slip .band-navy { width: 50px; }

  /* Business cards */
  .card { width: 255px; height: 156px; }
  .card-front { left: 667px; top: 564px; }
  .card-front .brand { position: absolute; left: 10px; top: 60px; font-size: 11px; gap: 4px; }
  .card-front .brand-dot { width: 7px; height: 7px; }
  .card-front .holder { position: absolute; left: 120px; top: 12px; border-left: 1px solid var(--gold); padding-left: 6px; font-size: 6.5px; line-height: 1.4; color: var(--navy); white-space: nowrap; }
  .card-front .holder-name { color: var(--gold); font-size: 8.5px; }
  .card-front .holder-role { color: var(--gold); margin-bottom: 6px; }
  .card-front .licence { position: absolute; left: 26px; bottom: 14px; font-size: 5.5px; color: var(--navy); }
  .card-front .band { height: 5px; }
  .card-front .band-navy { width: 20px; }

  .card-back { top: 734px; height: 78px; display: flex; flex-direction: column; align-items: center; justify-content: center; gap: 18px; }
  .card-back .brand { font-size: 14px; }
  .card-back .brand-dot { width: 8px; height: 8px; }
  .card-back .web { font-size: 6.5px; }
  .card-back-navy { left: 667px; background: var(--navy); }
  .card-back-navy .brand, .card-back-navy .web { color: #fff; }
  .card-back-gold { left: 931px; width: 250px; background: var(--gold); }
  .card-back-gold .brand { color: #fff; }
  .card-back-gold .brand-dot { background: var(--navy); }
  .card-back-gold .web { color: #fff; }
</style>
</head>
<body>

<section class="sheet letterhead" aria-label="Letterhead">
  <div class="brand"><span class="brand-dot"></span>Norvel Partners</div>
  <address class="contact">
    Office 14, 3rd Floor<br>Harbor Point Tower<br>Westgate, Marlow<br>Phone: +00 12 3456 667<br>www.norvelpartners.com
  </address>
  <div class="footer-info">
    <span>www.norvelpartners.com</span>
    <span>Tel: +00 12 3456 667</span>
    <span>info@norvelpartners.com</span>
  </div>
  <div class="band"><span class="band-gold"></span><span class="band-light"></span><span class="band-navy"></span></div>
</section>

<section class="sheet slip" aria-label="Compliment slip">
  <div class="brand"><span class="brand-dot"></span>Norvel Partners</div>
  <address class="contact">
    Office 14, 3rd Floor<br>Harbor Point Tower<br>Westgate, Marlow
  </address>
  <div class="band"><span class="band-gold"></span><span class="band-light"></span><span class="band-navy"></span></div>
</section>

<section class="sheet card card-front" aria-label="Business card front">
  <div class="brand"><span class="brand-dot"></span>Norvel Partners</div>
  <address class="holder">
    <div class="holder-name">Elena Marsh</div>
    <div class="holder-role">Consultant</div>
    Office 14, 3rd Floor<br>Harbor Point Tower<br>Westgate, Marlow<br>Phone: +00 12 3456 667<br>Mob: +00 12 3456 210<br>elena.marsh@norvelpartners.com<br>www.norvelpartners.com
  </address>
  <div class="licence">Licence No. 48210</div>
  <div class="band"><span class="band-gold"></span><span class="band-navy"></span></div>
</section>

<section class="sheet card card-back card-back-navy" aria-label="Business card back, navy">
  <div class="brand"><span class="brand-dot"></span>Norvel Partners</div>
  <div class="web">www.norvelpartners.com</div>
</section>

<section class="sheet card card-back card-back-gold" aria-label="Business card back, gold">
  <div class="brand"><span class="brand-dot"></span>Norvel Partners</div>
  <div class="web">www.norvelpartners.com</div>
</section>

</body>
</html>
```